CBD Boutique Business Card Needed

We are in need of a business card to reflect the direction of our latest products. We are a fully organic company in which our store and products are very heavy in wood and "natural" components. We decided to bring color into one of our brands and immediately knew this is where we needed to go.

We are NOT a cash grab CBD company. We could have done this wrong, slapped a label on a shit product and left it like that. I am passionate about sharing my experience with other veterans and opening a store and making it a comfortable place for others to come and see if they can have the same experience.

Target Market(s)

We are a dual market company. We do have a beauty line that will cover the costs of the majority of our business. But we also heavily cater to veterans and first responders. I am a veteran and this is how I found out about CBD. So the marketing needs to bring in our higher end beauty clientele but also be able to not put off our customers that readily need this.

Contact Information for Business Card

What we are looking for is a light, professional, boutique design that is is neither quite feminine or masculine. Attached is a picture of a store in Portland that we asked our store designer to get her inspiration from. But all natural wood and black outlines are what is mostly in there.

Attached are the following files:

Logo: An AI file with how we have our logo. I do not understand AI and have no idea why the letters are individual. The font is Adam. OLU is the logo and Tonics of Vigor is our tagline.

KM Vantage (front and back) cards I did originally found at a trade show that I absolutely loved...while it is mostly there and I would still be happy with them but it is me pretending to be you. I understand I am not and there is probably a lot wrong that all of you would see instantly and this is why I am here.

Dropper Bottle: This is our final product mock up

Water Color: I am semi flexible here. This water color is slightly different on every level of our brand. The color itself can change...we are not stuck on THIS particular one. If you happen to make a new one that is similar in style and we use it...then I will happily commission you to change the rest on our next product run. I am pretty sure you can use this statement as evidence later . =) .

But seriously, we heavily believe in pay it forward and will work with anyone here that may have a vision bigger than ours. The winner of this contest will get preferential consideration on our marketing materials (need letterhead etc. next, as well as a brochure, and website) so three more projects coming down the pipeline.

Information to use for your mockup is contained on the card images I have included. I would prefer CBD for wellness CBD for life to be more prominent. No where else on the card do we have CBD mentioned.

Font styles to use
Sans Serif

Colors

Designer to choose colors to be used in the design.

Requirements
Must have
• Double Sided
• Front: OLU logo on front of card will be raised embossed. Background is watercolor. One has been provided. Others are up for consideration. If the rest of your design is incredible and I don't like your watercolor I will just ask to swap it.
• Back: Standard information. Not stuck on anything here. I LOVE clean minimal designs. The bleed on the card I provided is a luxury...
• Font for title and OLU is Adam. Everything else I prefer san serif or as clean as possible.
Nice to have
• I Need to incorporate Naturally Nurturing somewhere on the card. Bold but not intrusive.

```html
<!DOCTYPE html>
<html lang="en">
<head>
<meta charset="utf-8">
<title>OLU – Business Card</title>
<link rel="stylesheet" href="https://fonts.googleapis.com/css2?family=Oswald:wght@500&family=Work+Sans:wght@300;400;600&display=swap">
<style>
  :root {
    --backdrop: #ecebe7;
    --card: #fbfaf7;
    --ink: #1f2a2c;
    --ink-soft: #4a5557;
    --teal: #3f9ea6;
    --teal-deep: #2f7f86;
    --wash-1: rgba(95, 185, 192, 0.55);
    --wash-2: rgba(140, 205, 200, 0.45);
    --wash-3: rgba(180, 220, 226, 0.5);
  }
  * { box-sizing: border-box; margin: 0; padding: 0; }
  html, body {
    width: 1200px; height: 900px; overflow: hidden;
    background: var(--backdrop);
    font-family: "Work Sans", Arial, sans-serif;
    color: var(--ink);
  }
  .canvas { position: relative; width: 1200px; height: 900px; }
  .card {
    position: absolute; left: 250px; width: 700px; height: 400px;
    background: var(--card);
    border-bottom: 5px solid var(--teal);
    box-shadow: 0 2px 10px rgba(0, 0, 0, 0.08);
    overflow: hidden;
  }
  .card--front { top: 40px; }
  .card--back { top: 470px; }

  .watercolor {
    position: absolute; inset: 0;
    background:
      radial-gradient(ellipse 55% 60% at 20% 30%, var(--wash-1), transparent 70%),
      radial-gradient(ellipse 50% 55% at 80% 25%, var(--wash-3), transparent 70%),
      radial-gradient(ellipse 60% 50% at 60% 85%, var(--wash-2), transparent 70%),
      radial-gradient(ellipse 40% 45% at 10% 90%, var(--wash-3), transparent 70%),
      var(--card);
  }

  .brand { position: absolute; left: 0; right: 0; top: 95px; text-align: center; }
  .brand__name {
    font-weight: 300; font-size: 120px; line-height: 1; letter-spacing: 8px; color: var(--ink);
  }
  .brand__tagline {
    margin-top: 14px; font-weight: 300; font-size: 28px; letter-spacing: 4px;
    text-transform: uppercase; color: var(--ink);
  }
  .slogan {
    position: absolute; left: 0; right: 0; bottom: 32px; text-align: center;
    font-weight: 600; font-size: 18px; letter-spacing: 1.5px; color: var(--ink);
  }
  .slogan span + span { margin-left: 16px; }

  .motto {
    position: absolute; left: 0; right: 0; top: 52px; text-align: center;
    font-weight: 600; font-size: 15px; letter-spacing: 5px;
    text-transform: uppercase; color: var(--teal-deep);
  }
  .identity { position: absolute; right: 395px; top: 150px; text-align: right; }
  .identity__name {
    font-family: "Oswald", "Arial Narrow", sans-serif; font-weight: 500;
    font-size: 40px; line-height: 1; color: var(--teal); text-transform: uppercase;
  }
  .identity__role {
    margin-top: 6px; font-weight: 400; font-size: 20px; letter-spacing: 3px;
    color: var(--ink-soft); text-transform: uppercase;
  }
  .divider {
    position: absolute; left: 335px; top: 150px; width: 2px; height: 82px; background: var(--teal);
  }
  .contact { position: absolute; left: 360px; top: 152px; list-style: none; }
  .contact__item {
    display: flex; align-items: center; gap: 12px;
    font-size: 20px; letter-spacing: 1.5px; line-height: 27px; color: var(--ink);
  }
  .contact__item svg { width: 14px; height: 14px; flex: none; }
  .address {
    position: absolute; left: 38px; bottom: 24px;
    font-size: 19px; letter-spacing: 2px; color: var(--ink);
  }
</style>
</head>
<body>
<main class="canvas">
  <section class="card card--front" aria-label="Card front">
    <div class="watercolor" role="img" aria-label="Soft teal watercolor wash background"></div>
    <div class="brand">
      <p class="brand__name">OLU</p>
      <p class="brand__tagline">Tonics of Vigor</p>
    </div>
    <p class="slogan"><span>CBD FOR WELLNESS</span><span>CBD FOR LIFE</span></p>
  </section>

  <section class="card card--back" aria-label="Card back">
    <p class="motto">Naturally Nurturing</p>
    <div class="identity">
      <p class="identity__name">Dana Whitfield</p>
      <p class="identity__role">Owner / CEO</p>
    </div>
    <div class="divider"></div>
    <ul class="contact">
      <li class="contact__item">
        <svg viewBox="0 0 14 14" aria-hidden="true"><path d="M3 1 L5.5 1 L6.2 4 L4.6 5.2 Q5.8 8 8.8 9.4 L10 7.8 L13 8.5 L13 11 Q12.5 13 10.5 13 Q1 12 1 3.5 Q1 1.5 3 1 Z" fill="none" stroke="var(--teal)" stroke-width="1.3"/></svg>
        555.018.4420
      </li>
      <li class="contact__item">
        <svg viewBox="0 0 14 14" aria-hidden="true"><rect x="1" y="3" width="12" height="8" fill="none" stroke="var(--teal)" stroke-width="1.3"/><path d="M1 3 L7 8 L13 3" fill="none" stroke="var(--teal)" stroke-width="1.3"/></svg>
        hello@olu.life
      </li>
      <li class="contact__item">
        <svg viewBox="0 0 14 14" aria-hidden="true"><circle cx="7" cy="7" r="6" fill="none" stroke="var(--teal)" stroke-width="1.2"/><ellipse cx="7" cy="7" rx="2.6" ry="6" fill="none" stroke="var(--teal)" stroke-width="1"/><path d="M1 7 H13 M2 4 H12 M2 10 H12" stroke="var(--teal)" stroke-width="1"/></svg>
        www.olu.life
      </li>
    </ul>
    <p class="address">1420 N Cedar Ridge Ave Mesa, AZ 85201 Suite 200</p>
  </section>
</main>
</body>
</html>
```